K-VOR Landing Page

We want to re-design our current home page on our website (www.plexamora.com) to simplify it and reduce it down to the (3) main products / services we offer. There are too many options of where they can go and it seems to be confusing for them. Additionally, we sell a higher end software product and we want the site to appear very professional for when CFO's considering our software can be confident in its quality and the long established company that we are. Our products and services are all about optimizing manufacturing production for sheet metal stampers (primarily automotive and appliance). I am including a rough power point layout of what we are thinking along with flyers for our three main products. We want to maintain the look and feel of the sample marketing materials as much as possible but does not have to match exactly. We will be producing the video ourselves to add where the power point shows a video being. Please review our website for any additional information.

```html
<!DOCTYPE html>
<html lang="en">
<head>
<meta charset="utf-8">
<title>K-VOR Solutions</title>
<link href="https://fonts.googleapis.com/css2?family=Bebas+Neue&family=Roboto:wght@400;500;700&family=Roboto+Condensed:wght@700&display=swap" rel="stylesheet">
<style>
:root{
  --blue:#2c6782;
  --blue-dark:#1a4d66;
  --yellow:#fdc316;
  --yellow-soft:#fcd25a;
  --charcoal:#2b292a;
  --gray:#6f6f72;
  --ink:#2d2b2b;
  --white:#ffffff;
  --link-blue:#2b6680;
}
*{box-sizing:border-box;margin:0;padding:0}
html,body{width:1200px;height:2368px;overflow:hidden}
body{position:relative;background:var(--white);font-family:'Roboto',sans-serif;color:var(--ink)}
.abs{position:absolute}

/* header */
.brand{left:111px;top:30px;font:700 52px/60px 'Roboto',sans-serif;color:var(--charcoal);letter-spacing:1px}
.call-icon{left:767px;top:34px;width:56px;height:56px;border-radius:50%;background:var(--white);box-shadow:0 6px 16px rgba(0,0,0,.15);display:flex;align-items:center;justify-content:center}
.call-text{left:845px;top:48px;font:500 23px/28px 'Roboto',sans-serif;color:var(--link-blue)}

.main-nav{left:111px;top:119px;width:978px;height:53px;border-radius:6px;background:linear-gradient(#5a5a5c,#2a2829);display:flex;justify-content:space-around;align-items:center;padding:0 16px;z-index:3}
.main-nav a{color:var(--white);text-decoration:none;font:700 14px 'Roboto Condensed',sans-serif;text-transform:uppercase}

/* hero */
.hero-bg{left:0;top:145px;width:1200px;height:690px}
.hero-kicker{left:111px;top:282px;font:26px/32px 'Bebas Neue',sans-serif;color:var(--yellow)}
.hero-title{left:111px;top:316px;font:58px/62px 'Bebas Neue',sans-serif;color:var(--white)}
.hero-copy{left:111px;top:396px;width:430px;font:400 20px/31px 'Roboto',sans-serif;color:var(--white)}
.video-frame{left:986px;top:545px;width:128px;height:128px;border:2px solid var(--yellow)}
.video{left:600px;top:279px;width:489px;height:368px;border:3px solid var(--white);background:radial-gradient(circle at 60% 35%,#7a5a3c,#2c2622 55%,#111 100%)}
.play{left:814px;top:432px;width:58px;height:58px;border-radius:50%;background:var(--white);display:flex;align-items:center;justify-content:center}

/* products */
.section-title{font:68px/72px 'Bebas Neue',sans-serif;color:var(--ink)}
.products-title{left:0;width:1200px;top:920px;text-align:center}
.card{top:1048px;width:305px;height:523px;text-align:center;padding:0 14px}
.card-blue{left:111px;background:linear-gradient(#4c7e94,#1b5069);color:var(--white);border-radius:40px 40px 40px 0}
.card-yellow{left:448px;background:linear-gradient(#fdd15a,#fdc316);color:var(--ink);border-radius:40px 40px 0 40px}
.card-gray{left:784px;background:linear-gradient(#7a7a7d,#262425);color:var(--white);border-radius:40px 40px 0 40px}
.card-icon{width:94px;height:94px;border-radius:50%;margin:41px auto 0;display:flex;align-items:center;justify-content:center;background:var(--white)}
.card-yellow .card-icon{background:var(--charcoal)}
.card-title{margin-top:24px;font:700 17px/27px 'Roboto',sans-serif;text-transform:uppercase}
.card-dot{width:7px;height:7px;border-radius:50%;background:rgba(200,200,200,.7);margin:6px auto 10px}
.card-copy{font:400 16.5px/26px 'Roboto',sans-serif;height:201px}
.card-btn{display:inline-block;margin-top:14px;width:188px;height:49px;line-height:45px;border:2px solid currentColor;border-radius:3px;font:500 15.5px/45px 'Roboto',sans-serif;text-transform:uppercase;color:inherit;text-decoration:none}

/* guarantee */
.footer-bg{left:0;top:1845px;width:1200px;height:523px;background:linear-gradient(#6f6f72,#302e2f 55%,#262425);border-radius:60px 60px 0 0}
.guarantee{left:43px;top:1697px;width:1114px;height:300px;background:linear-gradient(120deg,#fcd35f,#f6c62e);border-radius:150px 0 150px 0}
.guarantee-badge{left:60px;top:1714px;width:265px;height:265px;background:var(--white);border-radius:132px 132px 132px 0;display:flex;align-items:center;justify-content:center;font:700 54px 'Roboto',sans-serif;color:var(--charcoal)}
.guarantee-title{left:404px;top:1764px}
.guarantee-copy{left:404px;top:1852px;width:680px;font:400 22px/33px 'Roboto',sans-serif;color:#22566e}

/* footer */
.footer-brand{left:111px;top:2118px;font:700 74px/80px 'Roboto',sans-serif;color:var(--white);letter-spacing:2px}
.foot-col{top:2062px;color:var(--white)}
.foot-col h3{font:700 20px/26px 'Roboto Condensed',sans-serif;text-transform:uppercase;margin-bottom:15px}
.foot-col ul{list-style:none}
.foot-col li{position:relative;padding-left:25px;font:500 14.5px/29px 'Roboto',sans-serif}
.foot-col li::before{content:"";position:absolute;left:1px;top:12px;width:5px;height:5px;border-radius:50%;background:var(--yellow)}
.col-nav{left:451px}
.col-links{left:682px}
.col-contact{left:859px}
.contact-row{display:flex;align-items:flex-start;margin-bottom:14px}
.contact-row .dotc{width:34px;height:34px;border-radius:50%;background:var(--yellow);flex:none;display:flex;align-items:center;justify-content:center;margin-right:17px}
.contact-row span{font:500 14.5px/21px 'Roboto',sans-serif;padding-top:6px}
.foot-rule{left:111px;top:2300px;width:978px;height:1px;background:rgba(255,255,255,.2)}
.copyright{left:0;width:1200px;top:2321px;text-align:center;font:400 15px/20px 'Roboto',sans-serif;color:var(--white)}
</style>
</head>
<body>

<div class="abs brand">K-VOR</div>
<div class="abs call-icon">
  <svg width="26" height="26" viewBox="0 0 24 24"><path fill="#fdc316" d="M6.6 10.8a15.1 15.1 0 0 0 6.6 6.6l2.2-2.2c.3-.3.7-.4 1-.2 1.1.4 2.3.6 3.6.6.6 0 1 .4 1 1V20c0 .6-.4 1-1 1A17 17 0 0 1 3 4c0-.6.4-1 1-1h3.5c.6 0 1 .4 1 1 0 1.3.2 2.5.6 3.6.1.3 0 .7-.2 1z"/></svg>
</div>
<div class="abs call-text">CALL US: 555-014-2277</div>

<nav class="abs main-nav">
  <a href="#">About</a><a href="#">How We Help</a><a href="#">K-VOR Software</a><a href="#">Transfer Simulation Service</a><a href="#">Business Case</a><a href="#">Resources</a><a href="#">Contact</a>
</nav>

<svg class="abs hero-bg" viewBox="0 0 1200 690">
  <defs><linearGradient id="heroGrad" x1="0" y1="0" x2="0" y2="1"><stop offset="0" stop-color="#3a7590"/><stop offset="1" stop-color="#1b4f67"/></linearGradient></defs>
  <path d="M0 0H1200V592L600 672L0 592Z" fill="url(#heroGrad)"/>
  <path d="M0 592L600 672L1200 592V604L600 686L0 604Z" fill="#fdc316"/>
</svg>

<div class="abs hero-kicker">Welcome to</div>
<h1 class="abs hero-title">K-VOR Solutions</h1>
<p class="abs hero-copy">At our core, we are a software company committed to providing cutting-edge simulation and optimization solutions. However, we understand that our customers have diverse needs and requirements which may not fit with buying software at this time. That’s why we offer flexible options for you to experience the power of K-VOR.</p>

<div class="abs video-frame"></div>
<div class="abs video" role="img" aria-label="Video of a transfer press line running stamping tooling"></div>
<div class="abs play"><svg width="22" height="24" viewBox="0 0 22 24"><path d="M3 2L20 12L3 22Z" fill="#111"/></svg></div>

<h2 class="abs section-title products-title">Our Products</h2>

<div class="abs card card-blue">
  <div class="card-icon"><svg width="44" height="44" viewBox="0 0 44 44" fill="none" stroke="#1f5570" stroke-width="2.5"><rect x="6" y="6" width="32" height="24" rx="2"/><path d="M22 30v6M14 38h16"/><path d="M22 11l6 3v6l-6 3-6-3v-6z"/></svg></div>
  <div class="card-title">New Tool Simulation and Optimization</div>
  <div class="card-dot"></div>
  <p class="card-copy">Are you starting a new transfer tooling program soon? Trust the experts at K-VOR to make it the best one you’ve ever had! Know your production rates before you build and confidently launch your tooling at the HIGHEST possible production rates!</p>
  <a class="card-btn" href="#">Request a Quote</a>
</div>

<div class="abs card card-yellow">
  <div class="card-icon"><svg width="46" height="46" viewBox="0 0 46 46" fill="none" stroke="#fdc316" stroke-width="3"><circle cx="23" cy="23" r="14" stroke-dasharray="5 3"/><circle cx="23" cy="23" r="9"/><path d="M17 27l4-4 3 2 5-6"/></svg></div>
  <div class="card-title">Existing Tool Optimization (With or Without CAD)</div>
  <div class="card-dot"></div>
  <p class="card-copy">Are you at capacity in your transfer press, running your equipment harder than you’d like, or simply know you can be doing better? Our existing tool optimization service is a great way increase your production efficiency (OEE) and free up press capacity.</p>
  <a class="card-btn" href="#">Request a Quote</a>
</div>

<div class="abs card card-gray">
  <div class="card-icon"><svg width="48" height="44" viewBox="0 0 48 44" fill="none" stroke="#3a3839" stroke-width="2.5"><rect x="4" y="6" width="30" height="22" rx="2"/><path d="M19 28v6M12 36h14"/><path d="M14 13l-4 4 4 4M24 13l4 4-4 4M21 12l-4 10"/><circle cx="38" cy="26" r="5"/></svg></div>
  <div class="card-title">K-VOR Software Products</div>
  <div class="card-dot"></div>
  <p class="card-copy">Without question, our most successful customers are the ones who use the software themselves. K-VOR Users typically see as much as 40% increase in their production rates! Hard to believe? Try it and see for yourself!</p>
  <a class="card-btn" href="#">Request a Quote</a>
</div>

<div class="abs footer-bg"></div>
<div class="abs guarantee" role="img" aria-label="Warm yellow backdrop of a stamping press floor"></div>
<div class="abs guarantee-badge">K-VOR</div>
<h2 class="abs section-title guarantee-title">Our Gaurantee</h2>
<p class="abs guarantee-copy">You’ll make your money back in your first (5) projects or we’ll refund the entire purchase price!</p>

<div class="abs footer-brand">K-VOR</div>

<div class="abs foot-col col-nav">
  <h3>Navigation</h3>
  <ul><li>About</li><li>How We Help</li><li>K-VOR Software</li><li>Transfer Simulation Service</li><li>Business Case</li><li>Resources</li></ul>
</div>
<div class="abs foot-col col-links">
  <h3>Quick Links</h3>
  <ul><li>Contact</li><li>Simulation Defined</li><li>Privacy Policy</li><li>Sitemap</li></ul>
</div>
<div class="abs foot-col col-contact">
  <h3>Contact Us</h3>
  <div class="contact-row"><div class="dotc"><svg width="14" height="16" viewBox="0 0 14 18"><path d="M7 0a7 7 0 0 0-7 7c0 5 7 11 7 11s7-6 7-11a7 7 0 0 0-7-7zm0 9.5A2.5 2.5 0 1 1 7 4.5a2.5 2.5 0 0 1 0 5z" fill="#2b292a"/></svg></div><span>PO Box 412 · 318 Harlan<br>Industrial Dr. · Brookvale,<br>MI 49001-0412</span></div>
  <div class="contact-row"><div class="dotc"><svg width="14" height="14" viewBox="0 0 24 24"><path fill="#2b292a" d="M6.6 10.8a15.1 15.1 0 0 0 6.6 6.6l2.2-2.2c.3-.3.7-.4 1-.2 1.1.4 2.3.6 3.6.6.6 0 1 .4 1 1V20c0 .6-.4 1-1 1A17 17 0 0 1 3 4c0-.6.4-1 1-1h3.5c.6 0 1 .4 1 1 0 1.3.2 2.5.6 3.6.1.3 0 .7-.2 1z"/></svg></div><span>555-014-2277</span></div>
  <div class="contact-row"><div class="dotc"><svg width="14" height="11" viewBox="0 0 16 12"><path fill="#2b292a" d="M0 0h16v12H0zM1.5 1.5 8 6.5l6.5-5" stroke="#fdc316" stroke-width="1.2"/></svg></div><span>info@plexamora.com</span></div>
</div>

<div class="abs foot-rule"></div>
<div class="abs copyright">© 2024 K-VOR® Solutions &nbsp;|&nbsp; All Rights Reserved</div>

</body>
</html>
```